Marta Business Card

My wife is going to start her own business with renting holiday appartments to tourists. She needs a design for a new business card... and a new web site.
Look at Stayvolt "Erholung auf dem Lindenwäldchen"

Target Market(s)

Give business card to prospects at any situation

Contact Information for Business Card

not sure what this means

Font styles to use
Script

Colors
fec41a
fee18a

Requirements
Must have
• My wife's handwriting is difficult to read:
Entspannen - Loslassen - Auftanken
Marta & das Lindenwäldchen
Urlaub an einem besonderen Ort
Marta Brecke
Grauer Pfad 7
18471 Alt Feldow
post@marta-brecke.de
www.lindenwaeldchen.net
Nice to have
• Beige background
Font like handwriting

```html
<!DOCTYPE html>
<html lang="de">
<head>
<meta charset="utf-8">
<title>Marta &amp; das Lindenwäldchen – Visitenkarte</title>
<link rel="stylesheet" href="https://fonts.googleapis.com/css2?family=Dancing+Script:wght@500;600&family=Montserrat:wght@400;600;700&display=swap">
<style>
  :root {
    --wine: #6c0b0b;
    --wine-deep: #5a0808;
    --paper: #ffffff;
    --cream: #f7f5f2;
    --ink: #0a0a0a;
    --page: #ffffff;
  }
  * { box-sizing: border-box; margin: 0; padding: 0; }
  html, body {
    width: 740px; height: 1200px; overflow: hidden;
    background: var(--page);
  }
  .sheet {
    position: relative; width: 740px; height: 1200px;
  }
  .card {
    position: absolute; left: 40px; width: 660px; height: 378px;
    background: radial-gradient(ellipse at 50% 40%, #741010 0%, var(--wine) 55%, var(--wine-deep) 100%);
    box-shadow: 2px 3px 5px rgba(0,0,0,.35);
    overflow: hidden;
    color: var(--paper);
    font-family: "Montserrat", sans-serif;
  }
  .card--front { top: 195px; }
  .card--back { top: 625px; }

  /* brand name in place of the mark */
  .brand {
    position: absolute; text-align: center;
    font-family: "Montserrat", sans-serif; font-weight: 600;
    color: var(--paper); letter-spacing: 1px;
  }
  .brand__dot {
    display: block; margin: 0 auto 10px;
    width: 34px; height: 34px; border-radius: 50%;
    background: var(--paper);
  }
  .card--front .brand { left: 0; right: 0; top: 62px; font-size: 24px; }
  .card--back .brand { left: 39px; width: 200px; top: 140px; font-size: 20px; }

  /* front */
  .motto {
    position: absolute; left: 110px; width: 439px; top: 189px; height: 63px;
    border-top: 1px solid rgba(255,255,255,.85);
    border-bottom: 1px solid rgba(255,255,255,.85);
    font-family: "Dancing Script", cursive; font-weight: 600;
    font-size: 33px; line-height: 61px; text-align: center; white-space: nowrap;
  }
  .claim {
    position: absolute; left: 0; right: 0; top: 262px;
    text-align: center; font-size: 21px; letter-spacing: .5px; font-weight: 400;
  }
  .front-band { position: absolute; left: 0; bottom: 0; width: 660px; height: 51px; }
  .front-url {
    position: absolute; left: 0; right: 0; bottom: 12px;
    text-align: center; font-weight: 700; font-size: 19px; letter-spacing: 2.4px;
  }

  /* back */
  .name-tab { position: absolute; left: 277px; top: 21px; width: 383px; height: 83px; }
  .name-tab__title {
    position: absolute; left: 321px; top: 28px; white-space: nowrap;
    font-family: "Dancing Script", cursive; font-weight: 600;
    font-size: 27px; color: var(--wine);
  }
  .name-tab__line {
    position: absolute; left: 322px; top: 70px;
    font-size: 14.5px; color: var(--wine); letter-spacing: .4px;
  }
  .contact-rail { position: absolute; left: 311px; top: 128px; }
  .contact-list {
    position: absolute; left: 358px; top: 134px; list-style: none;
  }
  .contact-list li {
    height: 51px; line-height: 24px;
    font-weight: 700; font-size: 17.5px; letter-spacing: .3px;
  }
  .back-wave { position: absolute; left: 0; bottom: 0; width: 660px; height: 50px; }
</style>
</head>
<body>
<main class="sheet">

  <section class="card card--front" aria-label="Vorderseite">
    <div class="brand"><span class="brand__dot"></span>Hotel Lindenwäldchen</div>
    <p class="motto">Entspannen Loslassen Auftanken</p>
    <p class="claim">Urlaub an einem besonderen Ort</p>
    <svg class="front-band" viewBox="0 0 660 51" aria-hidden="true">
      <rect x="0" y="25" width="660" height="26" fill="#ffffff"/>
      <path d="M122 51 L144 6 Q147 0 154 0 L506 0 Q513 0 516 6 L537 51 Z" fill="#0a0a0a"/>
    </svg>
    <p class="front-url">www.lindenwaeldchen.net</p>
  </section>

  <section class="card card--back" aria-label="Rückseite">
    <svg class="name-tab" viewBox="0 0 383 83" aria-hidden="true">
      <path d="M0 0 L383 0 L383 83 L40 83 Q30 83 25 74 Z" fill="#f7f5f2"/>
    </svg>
    <p class="name-tab__title">Marta &amp; das Lindenwäldchen</p>
    <p class="name-tab__line">Marta Brecke - Grauer Pfad 7</p>

    <div class="brand"><span class="brand__dot"></span>Lindenwäldchen</div>

    <svg class="contact-rail" width="36" height="190" viewBox="0 0 36 190" aria-hidden="true">
      <line x1="18" y1="18" x2="18" y2="171" stroke="#0a0a0a" stroke-width="2.5"/>
      <g fill="#ffffff" stroke="#0a0a0a" stroke-width="2.5">
        <circle cx="18" cy="18" r="16"/>
        <circle cx="18" cy="69" r="16"/>
        <circle cx="18" cy="120" r="16"/>
        <circle cx="18" cy="171" r="16"/>
      </g>
      <!-- phone -->
      <path d="M12.5 12 q1.5-1.5 3 0 l1.2 2 q.6 1.2-.5 2 l-.8.6 q1 2.6 3.4 3.9 l.7-.8 q.9-1 2-.4 l2 1.3 q1.4 1.4 0 2.8 q-1.6 1.6-4 .8 q-5.6-2.3-8-8 q-.8-2.4 1-4.2 Z" fill="#0a0a0a"/>
      <!-- envelope -->
      <rect x="10.5" y="63.5" width="15" height="11" rx="1.5" fill="#0a0a0a"/>
      <path d="M11 64.5 L18 70 L25 64.5" fill="none" stroke="#ffffff" stroke-width="1.3"/>
      <!-- pin -->
      <path d="M18 128 C14 122.5 12.5 120 12.5 117.5 a5.5 5.5 0 0 1 11 0 C23.5 120 22 122.5 18 128 Z" fill="#0a0a0a"/>
      <circle cx="18" cy="117.5" r="2" fill="#ffffff"/>
      <!-- globe -->
      <g fill="none" stroke="#0a0a0a" stroke-width="1.4">
        <circle cx="18" cy="171" r="7.5"/>
        <ellipse cx="18" cy="171" rx="3.2" ry="7.5"/>
        <line x1="10.5" y1="171" x2="25.5" y2="171"/>
        <line x1="12" y1="167" x2="24" y2="167"/>
        <line x1="12" y1="175" x2="24" y2="175"/>
      </g>
    </svg>
    <ul class="contact-list">
      <li>43 (4310) 58204</li>
      <li>post@marta-brecke.de</li>
      <li>18471 Alt Feldow</li>
      <li>www.lindenwaeldchen.net</li>
    </ul>

    <svg class="back-wave" viewBox="0 0 660 50" preserveAspectRatio="none" aria-hidden="true">
      <path d="M0 40 C10 15 60 5 100 10 C150 16 160 40 200 38 C240 36 250 18 290 18 C330 18 340 40 380 40 C420 40 430 20 470 20 C510 20 520 40 560 38 C600 36 620 18 660 20 L660 50 L0 50 Z" fill="#ffffff"/>
    </svg>
  </section>

</main>
</body>
</html>
```